Kick Ass, Edgy, Fun, E commerce Embroidery Company Business Card

Sleek and edgy business card layout. main logo on front with business description (Custom Embroidery, the file is submitted is supposed to look like stitching)
Name, address, phone numbers, social icons (Friendwall and Snapgrid) on back. The card will be black plastic and the front main logo will be printed Spot UV.

Target Market(s)

Small Business Owners

Contact Information for Business Card

Focused, not cluttered and sleek. Modern looking.

Font styles to use
Other font styles liked:
• Very clean and elegant

Colors
acd136

Requirements
Must have
• Custom Embroidery

our Tagline: Every Logo Has A Story - Thread Yours
Nice to have
• Social Icons for Friendwall and Snapgrid
Should not have
• Too much visual noise

```html
<!DOCTYPE html>
<html lang="en">
<head>
<meta charset="utf-8">
<title>ThreadRiot Business Card</title>
<link rel="stylesheet" href="https://fonts.googleapis.com/css2?family=Black+Ops+One&family=Raleway:wght@600;800;900&family=Saira+Extra+Condensed:wght@400&display=swap">
<style>
  :root {
    --backdrop: #e7e7e3;
    --card: #000000;
    --lime: #acd136;
    --brand-green: #5fb548;
    --white: #ffffff;
    --arc: #12140a;
  }
  html, body {
    margin: 0;
    width: 1200px;
    height: 1200px;
    overflow: hidden;
    background: var(--backdrop);
  }
  .canvas {
    position: relative;
    width: 1200px;
    height: 1200px;
  }
  .card {
    position: absolute;
    top: 277px;
    width: 401px;
    height: 652px;
    background: var(--card);
    border-radius: 16px;
    overflow: hidden;
    color: var(--white);
    text-align: center;
  }
  .card--front { left: 144px; }
  .card--back { left: 662px; }

  .brand-mark {
    position: absolute;
    left: 0;
    right: 0;
    display: flex;
    flex-direction: column;
    align-items: center;
  }
  .brand-mark__dot {
    border-radius: 50%;
    background: var(--brand-green);
  }
  .brand-mark__name {
    font-family: "Raleway", sans-serif;
    font-weight: 900;
    color: var(--white);
    text-transform: uppercase;
    line-height: 0.95;
    letter-spacing: 1px;
  }
  .card--front .brand-mark { top: 120px; }
  .card--front .brand-mark__dot { width: 70px; height: 70px; margin-bottom: 30px; }
  .card--front .brand-mark__name { font-size: 66px; }

  .service {
    position: absolute;
    left: 0;
    right: 0;
    top: 492px;
    font-family: "Black Ops One", sans-serif;
    color: var(--lime);
    font-size: 38px;
    line-height: 1.25;
    letter-spacing: 3px;
    margin: 0;
  }

  .company {
    position: absolute;
    top: 54px;
    left: 0;
    right: 0;
    margin: 0;
    font-family: "Raleway", sans-serif;
    font-weight: 600;
    font-size: 36px;
    color: var(--lime);
  }
  .contact {
    position: absolute;
    top: 102px;
    left: 0;
    right: 0;
    margin: 0;
    font-family: "Saira Extra Condensed", sans-serif;
    font-size: 25px;
    line-height: 28px;
    font-style: normal;
  }
  .contact__gap { display: block; height: 30px; }
  .social {
    position: absolute;
    top: 289px;
    left: 0;
    right: 0;
    display: flex;
    justify-content: center;
    gap: 16px;
    font-family: "Saira Extra Condensed", sans-serif;
    font-size: 18px;
  }
  .social__item { display: flex; align-items: center; gap: 6px; }
  .social__square { width: 16px; height: 16px; border: 2px solid var(--white); border-radius: 4px; }

  .back-arc { position: absolute; left: 0; top: 330px; }

  .card--back .brand-mark { top: 378px; }
  .card--back .brand-mark__dot { width: 44px; height: 44px; margin-bottom: 22px; }
  .card--back .brand-mark__name { font-size: 38px; }

  .tagline {
    position: absolute;
    top: 562px;
    left: 0;
    right: 0;
    margin: 0;
    font-family: "Raleway", sans-serif;
    font-weight: 800;
    font-size: 25px;
    line-height: 32px;
  }
  .tagline__accent { color: var(--lime); display: block; }
</style>
</head>
<body>
<main class="canvas">
  <section class="card card--front">
    <div class="brand-mark">
      <span class="brand-mark__dot"></span>
      <span class="brand-mark__name">Thread<br>Riot</span>
    </div>
    <p class="service">CUSTOM<br>EMBROIDERY</p>
  </section>

  <section class="card card--back">
    <h1 class="company">ThreadRiot Inc</h1>
    <address class="contact">
      4417 Forge Hollow Rd Ste 8<br>
      Millbrook, CO 80199
      <span class="contact__gap"></span>
      1-800-555-0142<br>
      hello@ThreadRiot.com<br>
      ThreadRiot.com
    </address>
    <div class="social">
      <span class="social__item"><span class="social__square"></span>Snapgrid</span>
      <span class="social__item"><span class="social__square"></span>Friendwall</span>
    </div>
    <svg class="back-arc" width="401" height="200" viewBox="0 0 401 200" aria-hidden="true">
      <path d="M0 130 Q200 -70 401 150" fill="none" stroke="var(--arc)" stroke-width="10"/>
    </svg>
    <div class="brand-mark">
      <span class="brand-mark__dot"></span>
      <span class="brand-mark__name">Thread<br>Riot</span>
    </div>
    <p class="tagline">Every Logo Has A Story<span class="tagline__accent">Thread Yours!</span></p>
  </section>
</main>
</body>
</html>
```